Note/Card sent to show appreciation to partners who worked with us to improve local communities

I'd like a simple note/card designed for a wide audience. Originally, I called this a "Thanksgiving Card," but it's really just a card to be sent around Thanksgiving, not specifically celebrating the Thanksgiving holiday. We plan to send the card out just prior to Thanksgiving 2017 (Nov. 24, 2017). I work at a regulated electric utility, and we'd like to say thank you to the many stakeholders who we partner with throughout the year to support initiatives that help to improve our state and create opportunities for economic growth. I'm interested mostly in the design of the card, not the simple verbiage on the inside.
Customers, charitable foundations, nonprofits, advocacy groups, industry associations, friends

```html
<!DOCTYPE html>
<html lang="en">
<head>
<meta charset="utf-8">
<title>Thank You Card Concepts</title>
<link rel="stylesheet" href="https://fonts.googleapis.com/css2?family=Amatic+SC:wght@400;700&family=Caveat:wght@400&family=Cutive+Mono&family=Dancing+Script:wght@600&family=Oswald:wght@400;700&family=Pacifico&family=Playfair+Display&display=swap">
<style>
  :root {
    --ink: #111111;
    --paper: #ffffff;
    --orange: #f5aa33;
    --slate: #666666;
    --grey-text: #555555;
    --sky: #c6dfe5;
    --frame-grey: #9a9a9a;
    --magenta: #a01a60;
    --navy: #141c5e;
    --thank-orange: #f28a1c;
    --lemon: #eef25a;
    --peach: #f7b55c;
  }
  * { margin: 0; padding: 0; box-sizing: border-box; }
  html, body { width: 1149px; height: 1200px; overflow: hidden; background: var(--paper); }
  .sheet { position: relative; width: 1149px; height: 1200px; }
  .card { position: absolute; }
  .line-text { position: absolute; left: 0; width: 100%; text-align: center; white-space: nowrap; line-height: 1; }
  .concept-number {
    position: absolute; font-family: "Caveat", cursive;
    font-size: 44px; color: var(--ink); line-height: 1;
  }

  /* Concept 1 */
  .card-spark { left: 32px; top: 40px; width: 570px; height: 411px; border: 3px solid var(--ink); background: var(--paper); }
  .card-spark .headline {
    position: absolute; left: 90px; top: 58px; width: 200px;
    font-family: "Amatic SC", sans-serif; font-weight: 400; font-size: 58px;
    color: var(--ink); text-align: center; line-height: 70px; letter-spacing: 1px;
  }
  .card-spark .bulb-art { position: absolute; left: 341px; top: 0; width: 150px; height: 362px; }

  /* Concept 2 */
  .card-grateful { left: 101px; top: 504px; width: 411px; height: 569px; border: 3px solid var(--ink); background: var(--paper); }
  .card-grateful .flourish { position: absolute; left: 91px; width: 224px; height: 22px; }
  .card-grateful .big {
    font-family: "Amatic SC", sans-serif; font-weight: 700; font-size: 68px;
    color: var(--orange); letter-spacing: 1px;
  }
  .card-grateful .for-row { position: absolute; left: 96px; top: 240px; width: 214px; height: 50px; }
  .card-grateful .for-row .rule { position: absolute; top: 26px; width: 62px; height: 2px; background: var(--orange); }
  .card-grateful .for-row .word {
    position: absolute; left: 0; width: 100%; top: 0; text-align: center;
    font-family: "Dancing Script", cursive; font-weight: 600; font-size: 44px; color: var(--orange); line-height: 1;
  }
  .card-grateful .holiday {
    font-family: "Caveat", cursive; font-weight: 400; font-size: 38px; color: var(--grey-text);
  }

  /* Concept 3 */
  .card-outlet { left: 652px; top: 24px; width: 389px; height: 537px; border: 3px solid var(--ink); background: var(--slate); }
  .card-outlet .mono { font-family: "Cutive Mono", monospace; font-size: 25px; color: var(--paper); }
  .card-outlet .outlet-art { position: absolute; left: 110px; top: 137px; width: 164px; height: 263px; }

  /* Concept 4 */
  .card-bright { left: 651px; top: 575px; width: 389px; height: 537px; border: 3px solid var(--frame-grey); background: var(--sky); overflow: hidden; }
  .card-bright .bulb-art { position: absolute; left: 54px; top: 76px; width: 280px; height: 386px; }
  .card-bright .want {
    font-family: "Oswald", sans-serif; font-weight: 700; font-size: 66px; color: var(--magenta);
    letter-spacing: -1px; transform: scaleY(1.1);
  }
  .card-bright .to { font-family: "Playfair Display", serif; font-size: 30px; color: var(--navy); }
  .card-bright .thank { font-family: "Pacifico", cursive; font-size: 44px; color: var(--thank-orange); }
  .card-bright .you { font-family: "Oswald", sans-serif; font-weight: 700; font-size: 58px; color: var(--navy); letter-spacing: 14px; }
  .card-bright .for { font-family: "Dancing Script", cursive; font-weight: 600; font-size: 48px; color: var(--lemon); }
  .card-bright .everything { font-family: "Amatic SC", sans-serif; font-weight: 700; font-size: 84px; color: var(--peach); letter-spacing: 2px; }
</style>
</head>
<body>
<main class="sheet">

  <section class="card card-spark">
    <p class="headline">THANKS<br>FOR<br>EVERYTHING!</p>
    <svg class="bulb-art" viewBox="0 0 150 362" role="img" aria-label="Illustration of a hanging glowing light bulb with a red heart inside">
      <defs>
        <radialGradient id="spark-glow" cx="50%" cy="80%" r="50%">
          <stop offset="0%" stop-color="#f4f000"/>
          <stop offset="100%" stop-color="#e8e04a"/>
        </radialGradient>
      </defs>
      <rect x="0" y="0" width="150" height="362" fill="url(#spark-glow)" opacity="0.55"/>
    </svg>
  </section>
  <span class="concept-number" style="left:612px; top:396px;">1</span>

  <section class="card card-grateful">
    <svg class="flourish" style="top:52px;" viewBox="0 0 224 22" role="img" aria-label="Decorative flourish divider">
      <rect x="0" y="6" width="224" height="10" rx="5" fill="#555555" opacity="0.35"/>
    </svg>
    <p class="line-text big" style="top:106px;">SO VERY</p>
    <p class="line-text big" style="top:162px;">THANKFUL</p>
    <div class="for-row">
      <span class="rule" style="left:0;"></span>
      <span class="word">for</span>
      <span class="rule" style="right:0;"></span>
    </div>
    <p class="line-text big" style="top:302px;">YOU</p>
    <svg class="flourish" style="top:406px;" viewBox="0 0 224 22" role="img" aria-label="Decorative flourish divider">
      <rect x="0" y="6" width="224" height="10" rx="5" fill="#555555" opacity="0.35"/>
    </svg>
    <p class="line-text holiday" style="top:450px;">Happy thanksgiving!</p>
  </section>
  <span class="concept-number" style="left:526px; top:1006px;">2</span>

  <section class="card card-outlet">
    <p class="line-text mono" style="top:42px;">We want to</p>
    <p class="line-text mono" style="top:72px;">thank you</p>
    <svg class="outlet-art" viewBox="0 0 164 263" role="img" aria-label="Illustration of a white electrical wall outlet">
      <rect x="0" y="0" width="164" height="263" rx="16" fill="#f2f2f2"/>
    </svg>
    <p class="line-text mono" style="top:453px;">for</p>
    <p class="line-text mono" style="top:482px;">everything</p>
  </section>
  <span class="concept-number" style="left:1058px; top:462px;">3</span>

  <section class="card card-bright">
    <svg class="bulb-art" viewBox="0 0 280 386" role="img" aria-label="Illustration of a large teal light bulb">
      <defs>
        <linearGradient id="bright-bulb" x1="0" y1="0" x2="0" y2="1">
          <stop offset="0%" stop-color="#74c2b9"/>
          <stop offset="100%" stop-color="#5e9fa0"/>
        </linearGradient>
      </defs>
      <rect x="0" y="0" width="280" height="386" rx="10" fill="url(#bright-bulb)"/>
    </svg>
    <p class="line-text want" style="top:44px;">WE WANT</p>
    <p class="line-text to" style="top:142px;">TO</p>
    <p class="line-text thank" style="top:190px;">thank</p>
    <p class="line-text you" style="top:268px; padding-left:14px;">YOU</p>
    <p class="line-text for" style="top:348px;">for</p>
    <p class="line-text everything" style="top:422px;">EVERYTHING</p>
  </section>
  <span class="concept-number" style="left:1056px; top:1046px;">4</span>

</main>
</body>
</html>
```